Quotation and Scripture Design

We are a marketing firm looking for a graphic designer who is gifted in the merging of typestyles, colors, and composition into images suitable for framing in the home or office. The design criteria is quite simple, (1) keep it fresh without looking dated or religious, and (2) push the envelope a little with good, solid graphic design. Phase one will involve building our inventory of original artwork to fifty or more pieces to be marketed online. For phase two in addition to a line of greeting cards, we will also offer art pieces reproduced by laser engravers, CNC routers, chemical etching, and digital printers. For this reason it is necessary that all art files be submitted in a vector format.

Target Market(s)

Professional women and men who appreciate and purchase gallery quality artwork.

Industry/Entity Type

Graphic Designer

Requirements
Must have
• Selection of the designer will be based on their graphic interruption of the following two quotations.
Quotation No. 1 - Romans 8:28
And we know that all things work together for good to those who love God, to those who are called according to His purpose.
Quotation No. 2 -Jeremiah 29:11
For I know the plans I have for you, declares the Lord. Plans to prosper you and not to harm you. Plans to give you hope and a future.
Design one of these two formats to fit a 8" x10" frame, and the other to fit a 12" x 12" frame.
Nice to have
• Rich colors, fresh typestyles . . . please no Times Roman. Bold, creative composition is what we are looking for.
Should not have
• Dated, religious artwork found in the local bible bookstore is a very good example of what we DO NOT want. If it is not something you would purchase for yourself or a friend, more than likely it won't meet our criteria.

```html
<!DOCTYPE html>
<html lang="en">
<head>
<meta charset="utf-8">
<title>Jeremiah 29:11 – Scripture Print</title>
<link rel="stylesheet" href="https://fonts.googleapis.com/css2?family=Forum&family=Kurale&family=Pinyon+Script&family=Source+Sans+3:wght@400&display=swap">
<style>
  :root {
    --page: #ffffff;
    --card: #ffffff;
    --card-edge: #f1f1f1;
    --shadow: rgba(40, 40, 40, 0.85);
    --gold: #f6c54c;
    --lavender: #c2b1e2;
    --rose: #e13a70;
    --teal: #4d8ea6;
  }
  * { margin: 0; padding: 0; box-sizing: border-box; }
  html, body {
    width: 856px;
    height: 1200px;
    overflow: hidden;
    background: var(--page);
  }
  .canvas {
    position: relative;
    width: 856px;
    height: 1200px;
  }
  .print {
    position: absolute;
    left: 48px;
    top: 158px;
    width: 720px;
    height: 720px;
    background: var(--card);
    border: 1px solid var(--card-edge);
    box-shadow: 8px 8px 4px var(--shadow);
  }
  .line {
    position: absolute;
    left: 85px;
    white-space: nowrap;
  }
  .reference {
    top: 100px;
    font-family: "Kurale", Georgia, serif;
    font-size: 27px;
    color: var(--gold);
  }
  .verse-open {
    font-family: "Forum", Georgia, serif;
    color: var(--lavender);
    text-transform: uppercase;
    line-height: 1;
  }
  .verse-open--small {
    top: 162px;
    font-size: 45px;
    letter-spacing: 0.5px;
  }
  .verse-open--large {
    top: 209px;
    font-size: 64px;
    letter-spacing: 0.5px;
  }
  .declaration {
    top: 270px;
    left: 98px;
    font-family: "Pinyon Script", cursive;
    font-size: 66px;
    color: var(--rose);
    line-height: 1.2;
  }
  .promise {
    top: 386px;
    font-family: "Source Sans 3", Arial, sans-serif;
    font-size: 27px;
    color: var(--teal);
  }
  .hope {
    font-family: "Kurale", Georgia, serif;
    font-size: 60px;
    color: var(--gold);
    line-height: 1;
  }
  .hope--first { top: 455px; }
  .hope--second { top: 535px; }
</style>
</head>
<body>
  <main class="canvas">
    <article class="print" aria-label="Jeremiah 29:11 scripture print">
      <p class="line reference">Jeremiah 29:11</p>
      <p class="line verse-open verse-open--small">For I know the plans</p>
      <p class="line verse-open verse-open--large">I have for you,</p>
      <p class="line declaration">declares the Lord.</p>
      <p class="line promise">Plans to prosper you and not to harm you.</p>
      <p class="line hope hope--first">Plans to give you</p>
      <p class="line hope hope--second">hope and a future.</p>
    </article>
  </main>
</body>
</html>
```